Our Joint Journey - Orthopedic needs from one site

We need slides that help to educate users, interest investors and allow the complexity of the entire continuum of care to be explained so anyone can understand. Our Joint Journey is a Varnolo Health Company. Ourjointjourneyhub.com. We allow people to evaluate, educate and engage with providers from one site. Simplyfying orthopedic care and wellness from one site. Patients, doctors, personal trainers, therapist, nutritionist, yoga, gyms, athletic trainers and more can connect from one site

Target Market(s)

Investors, Patients, Doctors and wellness providers

Industry/Entity Type

Healthcare

Requirements
Must have
• Investor slides, sales slides, education, process....

```html
<!DOCTYPE html>
<html lang="en">
<head>
<meta charset="utf-8">
<title>Our Joint Journey – Slides</title>
<link href="https://fonts.googleapis.com/css2?family=Montserrat:wght@500;600;700;800;900&family=Roboto:wght@400;500;700&display=swap" rel="stylesheet">
<style>
:root{
  --green:#47a84f;
  --green-soft:#5fb76a;
  --blue:#2a6cb8;
  --blue-deep:#245fa6;
  --ink:#222;
  --body:#555;
  --page:#dcdddf;
  --track:#f3f4f6;
}
*{box-sizing:border-box;margin:0;padding:0}
html,body{width:1200px;height:4065px;overflow:hidden}
body{background:var(--page);position:relative;font-family:'Roboto',sans-serif;color:var(--body)}
.slide{position:absolute;left:80px;width:1040px;height:584px;background:#fff;overflow:hidden}
.grad-panel{background:linear-gradient(135deg,var(--green-soft) 0%,#3f9f86 45%,#3d86c8 100%)}

/* cover */
.cover .side{position:absolute;left:685px;top:0;width:355px;height:584px}
.cover .photo{position:absolute;left:530px;top:134px;width:316px;height:316px;border-radius:50%;border:6px solid #fff;background:linear-gradient(140deg,#e9edf1,#b8c4cf 55%,#7d8e9e)}
.brand{position:absolute;left:54px;top:64px;display:flex;align-items:center;gap:14px}
.brand .dot{width:40px;height:40px;border-radius:50%;background:var(--green)}
.brand-name{font-family:'Montserrat',sans-serif;font-weight:700;color:var(--blue);font-size:30px;line-height:1.05;text-transform:uppercase}
.welcome{position:absolute;left:54px;top:236px;font-family:'Montserrat',sans-serif;font-weight:700;color:var(--blue);font-size:18px}
.cover h1{position:absolute;left:54px;top:270px;font-family:'Montserrat',sans-serif;font-weight:800;font-size:22px;color:#1c1c1c;white-space:nowrap}
.cover h1 .accent{color:var(--green);font-size:32px}
.cover .lead{position:absolute;left:54px;top:318px;width:430px;font-size:12.5px;line-height:20px;color:#444}
.socials{position:absolute;left:54px;top:387px;display:flex;gap:14px}
.socials span{width:38px;height:38px;border-radius:50%;background:linear-gradient(135deg,var(--green),var(--blue))}
.contact{position:absolute;top:511px;display:flex;align-items:center;gap:14px;font-size:13px;color:#333}
.contact .ic{width:38px;height:38px;border-radius:50%;background:linear-gradient(135deg,var(--green),var(--blue));display:flex;align-items:center;justify-content:center}
.contact.phone{font-weight:700;font-size:16px}

/* shared header/footer */
.top-rule{position:absolute;left:0;top:0;width:100%;height:6px;background:linear-gradient(to right,var(--green) 0 50%,var(--blue) 50%)}
.tab{position:absolute;left:390px;top:0;width:259px;height:84px}
.tab-name{position:absolute;left:470px;top:14px;font-family:'Montserrat',sans-serif;font-weight:700;color:#fff;font-size:16px;line-height:18px;text-transform:uppercase}
.tab-mark{position:absolute;left:430px;top:22px;width:28px;height:28px;border-radius:50%;border:2px solid #fff}
.foot-bar{position:absolute;left:237px;top:551px;width:567px;height:30px;background:var(--blue);color:#fff;font-size:9px;display:flex;align-items:center;justify-content:center}
.foot-rule{position:absolute;left:0;bottom:0;width:100%;height:4px;background:var(--blue)}
.slide-title{position:absolute;left:0;width:100%;text-align:center;top:113px;font-family:'Montserrat',sans-serif;font-weight:800;font-size:31px;color:var(--green)}
.title-rule{position:absolute;left:500px;top:161px;width:42px;height:3px;background:var(--blue)}
.intro{position:absolute;left:65px;width:910px;text-align:center;font-size:13px;line-height:21px;color:#555}

/* investor */
.portrait{position:absolute;left:74px;top:111px;width:388px;height:388px;border-radius:50%;border:9px solid var(--green);background:linear-gradient(170deg,#e8c6b4 0%,#b98f7a 35%,#6f7a3e 65%,#4b3d2c 100%)}
.investor .slide-title{left:529px;width:auto;top:148px;text-align:left}
.investor .title-rule{left:531px;top:198px}
.investor .copy{position:absolute;left:531px;top:222px;width:436px;font-size:13px;line-height:21.2px;text-align:justify;color:#555}

/* sales steps */
.step{position:absolute}
.step .bar{position:absolute;height:8px;width:148px}
.step .drop{position:absolute;width:8px;height:32px}
.step .notch{position:absolute;width:0;height:0;border-left:12px solid transparent;border-bottom:12px solid}
.step .badge{position:absolute;width:44px;height:44px;border-radius:50%;display:flex;align-items:center;justify-content:center}
.step .badge i{width:14px;height:14px;border-radius:50%;border:2px solid #fff}
.step .label{position:absolute;width:140px;text-align:center;font-size:11px;font-weight:700}
.step .rule{position:absolute;width:24px;height:2px}
.step .cap{position:absolute;width:130px;text-align:center;font-size:8.5px;line-height:11px;color:#666}
.step .stem{position:absolute;width:0;border-left:2px dotted}
.step .pin{position:absolute;width:7px;height:7px;border-radius:50%}
.blue-step{color:var(--blue)} .green-step{color:var(--green)}
.blue-step .bar,.blue-step .drop,.blue-step .badge,.blue-step .rule,.blue-step .pin{background:var(--blue)}
.green-step .bar,.green-step .drop,.green-step .badge,.green-step .rule,.green-step .pin{background:var(--green)}

/* education */
.education{background:linear-gradient(#fff 0%,#fff 50%,#eef2f6 100%)}
.education .scene{position:absolute;left:0;top:330px;width:1040px;height:254px;background:linear-gradient(100deg,#c9dceb 0%,#a9c4dd 30%,#e7c3a9 55%,#dcb196 70%,#8fb1d1 100%);-webkit-mask-image:linear-gradient(transparent,#000 35%);mask-image:linear-gradient(transparent,#000 35%)}
.education .intro{text-align:justify;text-align-last:center}

/* process */
.row{position:absolute;left:0;width:1040px;height:74px}
.row .txt{position:absolute;left:60px;width:232px;text-align:right;top:2px}
.row .txt b{display:block;font-size:15px;color:#1c1c1c;font-weight:700;margin-bottom:4px}
.row .txt span{font-size:12.5px;line-height:18px;color:#555}
.row .num{position:absolute;left:324px;top:0;width:113px;height:74px;border-radius:9px;color:#fff;font-family:'Montserrat',sans-serif;font-weight:700;font-size:30px;display:flex;align-items:center;justify-content:center}
.row .track{position:absolute;left:461px;top:11px;width:470px;height:52px;background:var(--track);border:1px solid #e3e5e8;border-right:none}
.row .fill{position:absolute;left:470px;top:20px;height:34px;color:#fff;font-size:11px;font-weight:700;padding-left:18px;display:flex;align-items:center}
.row svg{position:absolute;left:930px;top:8px}
.row.b .num,.row.b .fill{background:var(--blue)}
.row.g .num,.row.g .fill{background:var(--green)}

/* thanks */
.thanks .card{position:absolute;left:88px;top:153px;width:862px;height:280px;background:#fff;display:flex;align-items:center;justify-content:center;font-family:'Montserrat',sans-serif;font-weight:900;font-size:122px;letter-spacing:-2px}
.thanks .g{color:var(--green)} .thanks .b{color:var(--blue);margin-left:28px}
</style>
</head>
<body>

<!-- Cover -->
<section class="slide cover" style="top:84px">
  <div class="side grad-panel"></div>
  <div class="photo" role="img" aria-label="Photo of two doctors reviewing an x-ray"></div>
  <div class="brand"><span class="dot"></span><div class="brand-name">Our<br>Joint<br>Journey</div></div>
  <div class="welcome">WELCOME TO</div>
  <h1>OUR <span class="accent">JOINT</span> JOURNEY</h1>
  <p class="lead">Lorem ipsum dolor sit amet, consectetur adipiscing elit, sed do eiusmod tempor incididunt ut labore et dolore magna aliqua.</p>
  <div class="socials"><span></span><span></span><span></span><span></span></div>
  <div class="contact" style="left:54px">
    <span class="ic"><svg width="16" height="12" viewBox="0 0 16 12"><rect x="0.5" y="0.5" width="15" height="11" rx="1" fill="#fff"/><path d="M1 1l7 6 7-6" stroke="#3f8fa0" stroke-width="1.4" fill="none"/></svg></span>
    info@ourjointjourneyhub.com
  </div>
  <div class="contact phone" style="left:321px">
    <span class="ic"><svg width="16" height="16" viewBox="0 0 24 24"><path fill="#fff" d="M6.6 10.8a15 15 0 006.6 6.6l2.2-2.2c.3-.3.7-.4 1-.2 1.1.4 2.3.6 3.6.6.6 0 1 .4 1 1V20c0 .6-.4 1-1 1A17 17 0 013 4c0-.6.4-1 1-1h3.5c.6 0 1 .4 1 1 0 1.3.2 2.5.6 3.6.1.3 0 .7-.2 1z"/></svg></span>
    +1 555 010 2040
  </div>
</section>

<!-- Investor -->
<section class="slide investor" style="top:747px">
  <div class="top-rule"></div>
  <svg class="tab" viewBox="0 0 259 84"><defs><linearGradient id="tg1" x1="0" x2="1"><stop offset="0" stop-color="#47a84f"/><stop offset="1" stop-color="#2a6cb8"/></linearGradient></defs><polygon points="0,0 259,0 234,84 24,84" fill="url(#tg1)"/></svg>
  <span class="tab-mark"></span><div class="tab-name">Our<br>Joint<br>Journey</div>
  <div class="portrait" role="img" aria-label="Photo of a hiker with crutches looking over a valley"></div>
  <h2 class="slide-title">INVESTOR</h2>
  <div class="title-rule"></div>
  <p class="copy">Sed ut perspiciatis unde omnis iste natus error sit voluptatem accusantium doloremque laudantium, totam rem aperiam, eaque ipsa quae ab illo inventore veritatis et quasi architecto beatae vitae dicta sunt explicabo. Nemo enim ipsam voluptatem quia voluptas sit aspernatur aut odit aut fugit, sed quia consequuntur magni dolores eos qui ratione voluptatem sequi nesciunt. Neque porro quisquam est, qui dolorem ipsum quia dolor sit amet, consectetur, adipisci velit, sed quia non numquam eius modi tempora incidunt ut labore et dolore magnam aliquam quaerat voluptatem. Ut enim ad minima veniam, quis nostrum exercitationem ullam corporis suscipit laboriosam, nisi ut aliquid ex ea commodi consequatur</p>
  <div class="foot-bar">© 2022 Our Joint Journey. All Rights Reserved</div>
  <div class="foot-rule"></div>
</section>

<!-- Sales -->
<section class="slide sales" style="top:1410px">
  <div class="top-rule"></div>
  <svg class="tab" viewBox="0 0 259 84"><defs><linearGradient id="tg2" x1="0" x2="1"><stop offset="0" stop-color="#47a84f"/><stop offset="1" stop-color="#2a6cb8"/></linearGradient></defs><polygon points="0,0 259,0 234,84 24,84" fill="url(#tg2)"/></svg>
  <span class="tab-mark"></span><div class="tab-name">Our<br>Joint<br>Journey</div>
  <h2 class="slide-title">SALES</h2>
  <div class="title-rule"></div>
  <p class="intro" style="top:181px">Sed ut perspiciatis unde omnis iste natus error sit voluptatem accusantium doloremque laudantium, totam rem aperiam, eaque ipsa quae ab illo inventore veritatis et quasi architecto beatae vitae dicta sunt explicabo. Nemo enim ipsam voluptatem quia voluptas</p>

  <div class="step blue-step" style="left:55px;top:321px">
    <div class="badge" style="left:48px;top:0"><i></i></div>
    <div class="label" style="left:0;top:52px">Lorem ipsum dolor</div>
    <div class="rule" style="left:58px;top:69px"></div>
    <div class="cap" style="left:5px;top:75px">Sed ut perspiciatis unde omnis iste natus error sit</div>
    <div class="stem" style="left:69px;top:102px;height:50px"></div>
    <div class="pin" style="left:67px;top:109px"></div>
    <div class="bar" style="left:0;top:159px"></div>
    <div class="drop" style="left:0;top:159px"></div>
    <div class="notch" style="left:136px;top:147px"></div>
  </div>
  <div class="step green-step" style="left:208px;top:300px">
    <div class="badge" style="left:48px;top:0"><i></i></div>
    <div class="label" style="left:0;top:52px">Lorem ipsum dolor</div>
    <div class="rule" style="left:58px;top:69px"></div>
    <div class="cap" style="left:5px;top:75px">Sed ut perspiciatis unde omnis iste natus error sit</div>
    <div class="stem" style="left:69px;top:102px;height:50px"></div>
    <div class="pin" style="left:67px;top:109px"></div>
    <div class="bar" style="left:0;top:159px"></div>
    <div class="drop" style="left:0;top:159px"></div>
    <div class="notch" style="left:136px;top:147px"></div>
  </div>
  <div class="step blue-step" style="left:361px;top:279px">
    <div class="badge" style="left:48px;top:0"><i></i></div>
    <div class="label" style="left:0;top:52px">Lorem ipsum dolor</div>
    <div class="rule" style="left:58px;top:69px"></div>
    <div class="cap" style="left:5px;top:75px">Sed ut perspiciatis unde omnis iste natus error sit</div>
    <div class="stem" style="left:69px;top:102px;height:50px"></div>
    <div class="pin" style="left:67px;top:109px"></div>
    <div class="bar" style="left:0;top:159px"></div>
    <div class="drop" style="left:0;top:159px"></div>
    <div class="notch" style="left:136px;top:147px"></div>
  </div>
  <div class="step green-step" style="left:514px;top:258px">
    <div class="badge" style="left:48px;top:0"><i></i></div>
    <div class="label" style="left:0;top:52px">Lorem ipsum dolor</div>
    <div class="rule" style="left:58px;top:69px"></div>
    <div class="cap" style="left:5px;top:75px">Sed ut perspiciatis unde omnis iste natus error sit</div>
    <div class="stem" style="left:69px;top:102px;height:50px"></div>
    <div class="pin" style="left:67px;top:109px"></div>
    <div class="bar" style="left:0;top:159px"></div>
    <div class="drop" style="left:0;top:159px"></div>
    <div class="notch" style="left:136px;top:147px"></div>
  </div>
  <div class="step blue-step" style="left:667px;top:237px">
    <div class="badge" style="left:48px;top:0"><i></i></div>
    <div class="label" style="left:0;top:52px">Lorem ipsum dolor</div>
    <div class="rule" style="left:58px;top:69px"></div>
    <div class="cap" style="left:5px;top:75px">Sed ut perspiciatis unde omnis iste natus error sit</div>
    <div class="stem" style="left:69px;top:102px;height:50px"></div>
    <div class="pin" style="left:67px;top:109px"></div>
    <div class="bar" style="left:0;top:159px"></div>
    <div class="drop" style="left:0;top:159px"></div>
    <div class="notch" style="left:136px;top:147px"></div>
  </div>
  <div class="step green-step" style="left:820px;top:216px">
    <div class="badge" style="left:48px;top:0"><i></i></div>
    <div class="label" style="left:0;top:52px">Lorem ipsum dolor</div>
    <div class="rule" style="left:58px;top:69px"></div>
    <div class="cap" style="left:5px;top:75px">Sed ut perspiciatis unde omnis iste natus error sit</div>
    <div class="stem" style="left:69px;top:102px;height:50px"></div>
    <div class="pin" style="left:67px;top:109px"></div>
    <div class="bar" style="left:0;top:159px"></div>
    <div class="drop" style="left:0;top:159px"></div>
  </div>

  <div class="foot-bar">© 2022 Our Joint Journey. All Rights Reserved</div>
  <div class="foot-rule"></div>
</section>

<!-- Education -->
<section class="slide education" style="top:2073px">
  <div class="scene" role="img" aria-label="Photo of a therapist examining a patient's knee"></div>
  <div class="top-rule"></div>
  <svg class="tab" viewBox="0 0 259 84"><defs><linearGradient id="tg3" x1="0" x2="1"><stop offset="0" stop-color="#47a84f"/><stop offset="1" stop-color="#2a6cb8"/></linearGradient></defs><polygon points="0,0 259,0 234,84 24,84" fill="url(#tg3)"/></svg>
  <span class="tab-mark"></span><div class="tab-name">Our<br>Joint<br>Journey</div>
  <h2 class="slide-title">EDUCATION</h2>
  <div class="title-rule"></div>
  <p class="intro" style="top:183px">Sed ut perspiciatis unde omnis iste natus error sit voluptatem accusantium doloremque laudantium, totam rem aperiam, eaque ipsa quae ab illo inventore veritatis et quasi architecto beatae vitae dicta sunt explicabo. Nemo enim ipsam voluptatem quia voluptas sit aspernatur aut odit aut fugit, sed quia consequuntur magni dolores eos qui ratione voluptatem sequi nesciunt. Neque porro quisquam est, qui dolorem ipsum quia dolor sit amet, consectetur, adipisci velit, sed quia non numquam eius modi tempora incidunt ut labore et dolore magnam aliquam quaerat voluptatem. Ut enim ad minima veniam, quis nostrum exercitationem ullam corporis suscipit laboriosam, nisi ut aliquid ex ea commodi consequatur Quis autem vel eum iure reprehenderit qui in ea voluptate velit esse quam nihil molestiae consequatur, vel illum qui dolorem eum fugiat quo voluptas nulla pariatur</p>
  <div class="foot-bar">© 2022 Our Joint Journey. All Rights Reserved</div>
  <div class="foot-rule"></div>
</section>

<!-- Process -->
<section class="slide process" style="top:2736px">
  <div class="top-rule"></div>
  <svg class="tab" viewBox="0 0 259 84"><defs><linearGradient id="tg4" x1="0" x2="1"><stop offset="0" stop-color="#47a84f"/><stop offset="1" stop-color="#2a6cb8"/></linearGradient></defs><polygon points="0,0 259,0 234,84 24,84" fill="url(#tg4)"/></svg>
  <span class="tab-mark"></span><div class="tab-name">Our<br>Joint<br>Journey</div>
  <h2 class="slide-title" style="left:25px">PROCESS</h2>

  <div class="row b" style="top:182px">
    <div class="txt"><b>Lorem ipsum dolor sit</b><span>Sed ut perspiciatis unde omnis iste natus error sit voluptatem</span></div>
    <div class="num">01</div><div class="track"></div>
    <div class="fill" style="width:240px">60%</div>
    <svg width="34" height="58" viewBox="0 0 34 58"><path d="M2 2l28 27L2 56" fill="none" stroke="#2a6cb8" stroke-width="2.5"/></svg>
  </div>
  <div class="row g" style="top:274px">
    <div class="txt"><b>Lorem ipsum dolor sit</b><span>Sed ut perspiciatis unde omnis iste natus error sit voluptatem</span></div>
    <div class="num">02</div><div class="track"></div>
    <div class="fill" style="width:120px">30%</div>
    <svg width="34" height="58" viewBox="0 0 34 58"><path d="M2 2l28 27L2 56" fill="none" stroke="#47a84f" stroke-width="2.5"/></svg>
  </div>
  <div class="row b" style="top:366px">
    <div class="txt"><b>Lorem ipsum dolor sit</b><span>Sed ut perspiciatis unde omnis iste natus error sit voluptatem</span></div>
    <div class="num">03</div><div class="track"></div>
    <div class="fill" style="width:320px">80%</div>
    <svg width="34" height="58" viewBox="0 0 34 58"><path d="M2 2l28 27L2 56" fill="none" stroke="#2a6cb8" stroke-width="2.5"/></svg>
  </div>
  <div class="row g" style="top:458px">
    <div class="txt"><b>Lorem ipsum dolor sit</b><span>Sed ut perspiciatis unde omnis iste natus error sit voluptatem</span></div>
    <div class="num">04</div><div class="track"></div>
    <div class="fill" style="width:200px">50%</div>
    <svg width="34" height="58" viewBox="0 0 34 58"><path d="M2 2l28 27L2 56" fill="none" stroke="#47a84f" stroke-width="2.5"/></svg>
  </div>

  <div class="foot-bar">© 2022 Our Joint Journey. All Rights Reserved</div>
  <div class="foot-rule"></div>
</section>

<!-- Thank you -->
<section class="slide thanks grad-panel" style="top:3399px">
  <div class="card"><span class="g">THANK</span><span class="b">YOU</span></div>
</section>

</body>
</html>
```